Harbour Vale Lettings Web Site Design

I am after a very simple 3 page web site please. I attach a PDF with the text and information. The logo is also in the PDF. The colours should be orange and blues. The pages should be HOME - LANDLORDS - TENANTS.
Lettings and Property Management Company aimed at just being a reference point for tenants but more of a sales pitch to landlords. Please refer to the attached PDF and word file which contains far more content for the various pages.

Target Market(s)

Prospective Landlords mainly but tenants also

Industry/Entity Type

Lettings and Property Management

Number of Pages Required

3 page

Font styles to use
Sans Serif
Other font styles liked:
• Candara

Colors
0054AA
0677BA
7BADD7
CADEEF
E8F1F8
F0912C
F2A743
F7CA91
FBE8D2
FDF5EE

Requirements
Must have
• Must be colour co-ordinated to the logo (orange and dark blue predominently, Must have good quality stock images relating to property and renting out property. Should have home page and links to landlord page and tenant page. Must have the 4 logos that we are affiliated to (TKR, Tenancy Settle, BNF and Funds Guard Scheme) - all attached.
Nice to have
• Modern feel, crisp and sharp but simple - good stock images.

```html
<!DOCTYPE html>
<html lang="en">
<head>
<meta charset="utf-8">
<title>Harbour Vale Lettings</title>
<link href="https://fonts.googleapis.com/css2?family=Cinzel:wght@600;700&family=Montserrat:wght@400;500;600;700&display=swap" rel="stylesheet">
<style>
:root{
  --navy:#13305f;
  --navy-deep:#0f2650;
  --blue:#0054aa;
  --teal:#1aa3c9;
  --sky:#7badd7;
  --sky-pale:#cadeef;
  --ice:#e8f1f8;
  --orange:#f0912c;
  --orange-soft:#f2a743;
  --grey-bg:#f2f3f5;
  --ink:#1c2a3f;
  --muted:#4a5566;
  --white:#ffffff;
}
*{margin:0;padding:0;box-sizing:border-box}
html,body{width:679px;height:1200px;overflow:hidden}
body{font-family:"Montserrat",Arial,sans-serif;color:var(--ink);background:var(--white);position:relative}
.serif{font-family:"Cinzel",Georgia,serif}

/* hero */
.hero{position:absolute;left:0;top:0;width:679px;height:400px;overflow:hidden}
.hero-photo{position:absolute;inset:0;
  background:
   linear-gradient(100deg,rgba(255,255,255,.92) 0%,rgba(255,255,255,.55) 38%,rgba(255,255,255,0) 55%),
   linear-gradient(160deg,#dcebf7 0%,#9cc6e8 40%,#3f86c4 62%,#1f5f9e 80%,#7fb3dd 100%)}
.site-header{position:absolute;left:0;top:0;width:679px;height:70px}
.brand{position:absolute;left:34px;top:26px;display:flex;align-items:center;gap:7px}
.brand-mark{width:14px;height:14px;background:var(--orange)}
.brand-name{font-size:10px;font-weight:700;color:var(--navy);letter-spacing:.5px;text-transform:uppercase}
.main-nav{position:absolute;left:296px;top:33px;display:flex;gap:34px}
.main-nav a{font-size:8.5px;font-weight:700;color:var(--white);text-decoration:none;letter-spacing:.3px}
.btn{display:inline-block;border-radius:20px;font-size:8px;font-weight:700;color:var(--white);text-decoration:none;text-align:center;text-transform:uppercase;letter-spacing:.3px}
.btn-orange{background:var(--orange)}
.btn-teal{background:var(--teal)}
.enquiry-btn{position:absolute;left:500px;top:25px;width:104px;height:24px;line-height:24px}
.hero-title{position:absolute;left:34px;top:134px;font-size:27px;line-height:1.12;color:var(--navy-deep);font-weight:700}
.hero-text{position:absolute;left:34px;top:206px;width:265px;font-size:9px;line-height:1.55;color:var(--ink)}
.hero-actions{position:absolute;left:34px;top:250px;display:flex;gap:12px}
.hero-actions .btn{width:82px;height:26px;line-height:26px}
.hero-wave{position:absolute;left:0;top:330px}

/* about */
.about{position:absolute;left:0;top:440px;width:679px;height:290px}
.about-frame{position:absolute;left:66px;top:0;width:272px;height:250px;border:3px solid var(--navy);border-right:none;border-top:none}
.about-frame-top{position:absolute;left:66px;top:0;width:3px;height:20px;background:var(--navy)}
.about-photo{position:absolute;left:80px;top:22px;width:258px;height:220px;
  background:linear-gradient(135deg,#d9dde2 0%,#a9b6c4 45%,#6e7f93 100%)}
.about-body{position:absolute;left:372px;top:30px;width:270px}
.eyebrow{font-size:9px;font-weight:700;color:var(--teal);letter-spacing:1.2px;text-transform:uppercase}
.about-title{font-size:19px;color:var(--navy-deep);margin:4px 0 10px}
.about-body p{font-size:7.2px;line-height:1.6;color:var(--muted);margin-bottom:7px}
.about-body .btn{width:74px;height:22px;line-height:22px;margin-top:5px}

/* members */
.members{position:absolute;left:0;top:742px;width:679px;height:190px;background:var(--grey-bg);text-align:center}
.members .eyebrow{padding-top:22px;font-size:10px}
.members-title{font-size:21px;color:var(--navy-deep);margin-top:4px}
.badge-row{position:absolute;left:78px;top:96px;display:flex;gap:20px}
.badge{width:121px;height:70px;background:var(--white);display:flex;align-items:center;justify-content:center;box-shadow:0 2px 6px rgba(0,0,0,.06)}
.badge span{display:block}
.shape-green{width:34px;height:38px;background:#6fb33f}
.shape-teal{width:60px;height:20px;border-radius:10px;background:#2c9bb1}
.shape-navy{width:62px;height:30px;background:#1e2f5c}
.shape-ink{width:40px;height:40px;border-radius:50%;background:#1a2a4a}

/* footer */
.site-footer{position:absolute;left:0;top:940px;width:679px;height:260px;background:var(--navy);color:var(--white)}
.footer-nav{position:absolute;top:57px;left:0;width:679px;font-size:8px;font-weight:700}
.footer-nav a{position:absolute;color:var(--white);text-decoration:none}
.footer-brand{position:absolute;left:0;top:45px;width:679px;display:flex;flex-direction:column;align-items:center;gap:6px}
.footer-brand .brand-name{color:var(--white)}
.contact-row{position:absolute;left:0;top:150px;width:679px}
.contact{position:absolute;display:flex;align-items:flex-start;gap:9px}
.contact-icon{width:24px;height:24px;border-radius:50%;background:var(--white);display:flex;align-items:center;justify-content:center}
.contact h4{font-size:9px;font-weight:700;letter-spacing:.3px}
.contact p{font-size:7px;margin-top:3px;opacity:.85}
.footer-rule{position:absolute;left:34px;top:218px;width:611px;height:1px;background:rgba(255,255,255,.25)}
.copyright{position:absolute;left:34px;top:234px;font-size:7px;opacity:.8}
.social{position:absolute;right:34px;top:229px;display:flex;gap:6px}
.social span{width:14px;height:14px;border-radius:50%;background:var(--teal)}
</style>
</head>
<body>

<section class="hero">
  <div class="hero-photo" role="img" aria-label="Modern glass tower block rising into a bright blue sky"></div>
  <header class="site-header">
    <div class="brand"><span class="brand-mark"></span><span class="brand-name">Harbour Vale Lettings</span></div>
    <nav class="main-nav"><a href="#">HOME</a><a href="#">LANDLORDS</a><a href="#">TENANTS</a></nav>
    <a class="btn btn-orange enquiry-btn" href="#">Landlord Enquiry</a>
  </header>
  <h1 class="hero-title serif">Innovative &amp; Fresh<br>Property Management</h1>
  <p class="hero-text">Family-run lettings agency with over 20 years of experience, offering professional services for landlords and tenants in Eastbourne and surrounding areas.</p>
  <div class="hero-actions">
    <a class="btn btn-orange" href="#">Our Services</a>
    <a class="btn btn-teal" href="#">Contact Us</a>
  </div>
  <svg class="hero-wave" width="679" height="70" viewBox="0 0 679 70">
    <path d="M300 70 C420 40 560 18 679 0 L679 70 Z" fill="var(--navy)"/>
    <path d="M0 22 C180 58 420 62 679 24 L679 70 L0 70 Z" fill="var(--white)"/>
  </svg>
</section>

<section class="about">
  <div class="about-frame"></div>
  <div class="about-photo" role="img" aria-label="Letting agent going over paperwork with a couple at home"></div>
  <div class="about-body">
    <div class="eyebrow">Who We Are</div>
    <h2 class="about-title serif">Harbour Vale Lettings</h2>
    <p>Harbour Vale Lettings has emerged after over 20 years of privately managing our own rental properties. We are family run and decided to move all of our properties under one 'umbrella'. Now professionally set up as a legal entity, Harbour Vale is looking to welcome new tenants and landlords to an innovative and fresh way of letting property.</p>
    <p>We always maintain a high standard of service and our friendly and helpful team are experienced in all areas and offer an excellent service in helping landlords and tenants deal with problems and issues they face daily.</p>
    <p>Out of hours emergency service which means we are there to an emergency for our tenants and landlords 24/7.</p>
    <a class="btn btn-orange" href="#">Contact Us</a>
  </div>
</section>

<section class="members">
  <div class="eyebrow">We Are Proud Members Of</div>
  <h2 class="members-title serif">We Are Members Of or Affiliated To</h2>
  <div class="badge-row">
    <div class="badge" aria-label="TKR"><span class="shape-green"></span></div>
    <div class="badge" aria-label="Funds Guard Scheme"><span class="shape-teal"></span></div>
    <div class="badge" aria-label="Tenancy Settle"><span class="shape-navy"></span></div>
    <div class="badge" aria-label="BNF"><span class="shape-ink"></span></div>
  </div>
</section>

<footer class="site-footer">
  <nav class="footer-nav">
    <a href="#" style="left:128px">HOME</a>
    <a href="#" style="left:178px">LANDLORDS</a>
    <a href="#" style="left:430px">TENANTS</a>
    <a href="#" style="left:497px">CONTACT US</a>
  </nav>
  <div class="footer-brand"><span class="brand-mark"></span><span class="brand-name">Harbour Vale Lettings</span></div>
  <div class="contact-row">
    <div class="contact" style="left:98px">
      <span class="contact-icon"><svg width="12" height="12" viewBox="0 0 24 24"><path d="M12 2a7 7 0 0 0-7 7c0 5 7 13 7 13s7-8 7-13a7 7 0 0 0-7-7zm0 9.5A2.5 2.5 0 1 1 12 6.5a2.5 2.5 0 0 1 0 5z" fill="var(--navy)"/></svg></span>
      <div><h4>ADDRESS</h4><p>12 Harbour Road, Eastbourne</p></div>
    </div>
    <div class="contact" style="left:300px">
      <span class="contact-icon"><svg width="12" height="12" viewBox="0 0 24 24"><path d="M6.6 10.8a15 15 0 0 0 6.6 6.6l2.2-2.2a1 1 0 0 1 1-.25 11 11 0 0 0 3.6.6 1 1 0 0 1 1 1V20a1 1 0 0 1-1 1A17 17 0 0 1 3 4a1 1 0 0 1 1-1h3.5a1 1 0 0 1 1 1 11 11 0 0 0 .6 3.6 1 1 0 0 1-.25 1z" fill="var(--navy)"/></svg></span>
      <div><h4>PHONE</h4><p>01323 555 014</p></div>
    </div>
    <div class="contact" style="left:470px">
      <span class="contact-icon"><svg width="12" height="12" viewBox="0 0 24 24"><path d="M3 5h18v14H3z" fill="var(--navy)"/><path d="M3 5l9 7 9-7" fill="none" stroke="#fff" stroke-width="1.6"/></svg></span>
      <div><h4>EMAIL</h4><p>info@harbourvalelettings.com</p></div>
    </div>
  </div>
  <div class="footer-rule"></div>
  <p class="copyright">© 2023 Harbour Vale Lettings. All Rights Reserved.</p>
  <div class="social"><span></span><span></span><span></span><span></span></div>
</footer>

</body>
</html>
```